Rassemblons Nos Caissons

RassemblonsNosCaissons is crowdshipping marketplace that allows his members to get together to organize a container from country A to country B. Thereby they are able to import small volumes of products at low prices.

How it works: https://boxpoolfreight.example/Containers/

One example of website that we could use for reference: https://boxpoolfreight.example/

Target Market(s)

Crowdshipping - Freight forwarder -

Coding

Coded - Design and coding required

Number of Pages Required

3 page

Font styles to use
Sans Serif

Colors
f04a50
886aae
34a6d7
fbee3e
33b8a4

Requirements
Must have
• Landing page: https://boxpoolfreight.example/Containers/

Enquire: https://boxpoolfreight.example/Enquire/?subject=Space%20on%20container%20to%20Australia%20-%20Adelaide%20(22.08.2020)

```html
<!DOCTYPE html>
<html lang="en">
<head>
<meta charset="utf-8">
<title>Rassemblons Nos Caissons – Box Pool Freight</title>
<link rel="stylesheet" href="https://fonts.googleapis.com/css2?family=Poppins:wght@300;400;500;600;700&display=swap">
<style>
:root{
  --navy:#0f2557;
  --navy-deep:#0b1c45;
  --card-head:#2b3042;
  --ink:#1a1a1a;
  --text:#444a55;
  --grey-bg:#e7e7e7;
  --bar-track:#c5d0e4;
  --white:#ffffff;
}
*{box-sizing:border-box;margin:0;padding:0}
html,body{width:1200px;height:4392px;overflow:hidden}
body{font-family:"Poppins",sans-serif;color:var(--ink);background:var(--white);position:relative}
.abs{position:absolute}
a{color:inherit;text-decoration:none}

/* HERO */
.hero{position:absolute;left:0;top:0;width:1200px;height:690px;overflow:hidden}
.hero-photo{position:absolute;inset:0;background:linear-gradient(180deg,#9fb5c6 0%,#6f93ad 22%,#2f7f93 45%,#1f6f84 62%,#1e5d7a 80%,#173f66 100%)}
.hero-wave{position:absolute;left:0;top:540px;width:1200px;height:150px}
.brand{position:absolute;left:36px;top:34px;display:flex;align-items:center;gap:14px;color:var(--white)}
.brand-dot{width:56px;height:56px;border-radius:50%;background:var(--navy);flex:none}
.brand-name{font-weight:600;font-size:20px;line-height:26px;white-space:nowrap}
.header-phone{position:absolute;left:825px;top:20px;display:flex;align-items:center;gap:8px;color:var(--white);font-size:18px}
.btn-enquire{position:absolute;left:1036px;top:14px;width:110px;height:39px;background:var(--navy);color:var(--white);font-size:17px;display:flex;align-items:center;justify-content:center}
.main-nav{position:absolute;left:500px;top:94px;display:flex;color:var(--white);font-size:15px;font-weight:500}
.main-nav a{padding:0 20px;border-left:1px solid rgba(255,255,255,.45);line-height:18px}
.main-nav a:first-child{padding-left:0;border-left:none;text-decoration:underline;text-underline-offset:5px}
.main-nav a:last-child{padding-right:0}
.hero-title{position:absolute;left:0;width:1200px;text-align:center;color:var(--white)}
.hero-welcome{top:222px;font-size:46px;font-weight:500}
.hero-name{top:272px;font-size:58px;font-weight:600;letter-spacing:-1px}
.hero-find{top:362px;font-size:22px;font-weight:300}
.search{position:absolute;left:332px;top:423px;display:flex;height:50px}
.search-select{width:353px;background:var(--white);color:#666;font-size:17px;display:flex;align-items:center;justify-content:space-between;padding:0 20px}
.search-btn{width:183px;background:var(--navy);color:var(--white);font-size:17px;display:flex;align-items:center;justify-content:center}
.slide-arrow{position:absolute;top:315px;width:46px;height:46px;border-radius:50%}
.slide-arrow.prev{left:115px;border:2px solid rgba(255,255,255,.8)}
.slide-arrow.next{left:1042px;background:var(--navy)}
.slide-dots{position:absolute;left:565px;top:606px;display:flex;gap:26px}
.slide-dots span{width:12px;height:12px;border-radius:50%;border:2px solid #6c7689}
.slide-dots span+span+span{margin-left:-14px}

/* ABOUT */
.about-photo{position:absolute;left:170px;top:777px;width:324px;height:321px;border-radius:0 0 162px 162px;background:linear-gradient(180deg,#7fb6d8 0%,#d8e2ea 45%,#3c6f8f 75%,#2b5574 100%)}
.about-copy{position:absolute;left:608px;top:770px;width:468px}
.about-copy h2{font-size:38px;font-weight:600;margin-bottom:20px}
.about-copy p{font-size:15px;line-height:28px;color:var(--text);margin-bottom:12px}

/* CONTAINERS */
.containers{position:absolute;left:0;top:1200px;width:1200px;height:1660px;background:var(--grey-bg)}
.section-curve{position:absolute;left:0;width:1200px}
.containers-title{position:absolute;left:0;top:1290px;width:1200px;text-align:center;font-size:38px;font-weight:600}
.title-rule{position:absolute;left:569px;top:1349px;width:64px;height:4px;background:var(--navy)}
.card-grid{position:absolute;left:131px;top:1393px;display:grid;grid-template-columns:455px 455px;column-gap:40px;row-gap:41px}
.box-card{position:relative;height:406px;background:var(--white);box-shadow:0 2px 10px rgba(0,0,0,.06)}
.box-card-head{position:absolute;left:8px;top:8px;right:8px;height:131px;background:var(--card-head);color:var(--white);padding:28px 0 0 76px}
.box-flag{position:absolute;left:-12px;top:26px;width:73px;height:73px;background:linear-gradient(135deg,#1b2a78 0%,#2a3a8a 60%,#8a2b4a 100%);border:2px solid var(--white)}
.box-dest{font-size:22px;font-weight:500}
.box-space-head{font-size:18px;margin-top:8px;font-weight:300}
.box-body{position:absolute;left:28px;top:162px;width:392px}
.box-space{font-size:19px;color:var(--navy);font-weight:500}
.box-bar{margin-top:10px;height:7px;background:var(--bar-track);border-radius:4px}
.box-bar span{display:block;width:358px;height:7px;background:var(--navy);border-radius:4px}
.box-meta{display:flex;justify-content:space-between;margin-top:30px;font-size:14px;line-height:24px;color:#333}
.box-actions{display:flex;gap:9px;margin-top:34px;padding-left:49px}
.btn-outline,.btn-solid{height:38px;border-radius:19px;font-size:15px;display:flex;align-items:center;justify-content:center}
.btn-outline{width:131px;border:1.5px solid #b9c2d6;color:var(--navy)}
.btn-solid{width:162px;background:var(--navy);color:var(--white)}

/* HOW IT WORKS */
.how{position:absolute;left:0;top:2812px;width:1200px;height:660px;background:linear-gradient(90deg,#1a2c57 0%,#203b6c 45%,#2a4d7e 70%,#1b2f5c 100%);overflow:hidden}
.how-photo{position:absolute;inset:0;background:radial-gradient(ellipse at 55% 60%,rgba(190,200,215,.35),transparent 55%)}
.how-title{position:absolute;left:116px;top:3082px;color:var(--white);font-size:40px;font-weight:500}
.how-text{position:absolute;left:116px;top:3153px;width:370px;color:var(--white);font-size:15px;line-height:28px}
.step{position:absolute;width:256px;height:225px;background:var(--white);display:flex;flex-direction:column;align-items:center;justify-content:center;text-align:center;padding:0 30px;color:var(--navy);font-size:15px;line-height:25px;gap:14px}
.step-a{left:539px;top:2898px;transform:rotate(-2deg)}
.step-b{left:539px;top:3153px;transform:rotate(-2deg)}
.step-c{left:825px;top:3017px;transform:rotate(-2deg)}

/* ENQUIRY */
.enquiry-photo{position:absolute;left:179px;top:3561px;width:285px;height:327px;background:linear-gradient(180deg,#4d8fc8 0%,#9cc3e3 40%,#e6ecf0 58%,#55a7c7 72%,#2f7ea6 100%)}
.enquiry-title{position:absolute;left:503px;top:3580px;font-size:32px;font-weight:600}
.field{position:absolute;border:1.5px solid #b9bfca;font-size:15px;color:#888;padding:10px 16px}
.field-name{left:506px;top:3644px;width:256px;height:41px}
.field-email{left:779px;top:3644px;width:257px;height:41px}
.field-message{left:506px;top:3704px;width:530px;height:104px}
.btn-send{position:absolute;left:506px;top:3837px;width:176px;height:49px;background:var(--navy);color:var(--white);font-size:19px;display:flex;align-items:center;justify-content:center;gap:12px}

/* FOOTER */
.footer{position:absolute;left:0;top:4000px;width:1200px;height:392px;background:var(--navy-deep);color:var(--white)}
.footer-brand{position:absolute;left:100px;top:4112px;width:170px;text-align:center;font-size:16px;font-weight:600;line-height:22px;color:var(--white)}
.socials{position:absolute;left:124px;top:4214px;display:flex;gap:22px}
.socials span{width:18px;height:18px;border-radius:50%;border:1.5px solid var(--white)}
.foot-col{position:absolute;font-size:13px;line-height:20px;color:var(--white)}
.foot-col h4{font-size:15px;font-weight:600;margin-bottom:24px}
.contact-col{left:305px;top:4070px;width:280px}
.contact-row{display:flex;gap:12px;align-items:flex-start;margin-bottom:18px}
.company-col{left:651px;top:4070px;line-height:24.5px}
.company-col h4{margin-bottom:14px}
.company-col a{display:block}
.ask-col{left:862px;top:4070px;width:240px;line-height:22px}
.ask-col h4{margin-bottom:14px}
.btn-ask{display:flex;align-items:center;gap:14px;width:213px;height:45px;background:#1c3a78;margin-top:28px;border-radius:23px 0 0 23px;font-size:16px}
.btn-ask i{width:45px;height:45px;border-radius:50%;background:#06122f;display:flex;align-items:center;justify-content:center}
.foot-bar{position:absolute;left:0;top:4296px;width:1200px;height:1px;background:rgba(255,255,255,.15)}
.copyright{position:absolute;left:72px;top:4323px;font-size:14px;color:var(--white)}
.copyright strong{font-weight:600}
.legal{position:absolute;left:853px;top:4325px;font-size:13px;display:flex;gap:12px;color:var(--white)}
</style>
</head>
<body>

<!-- HERO -->
<section class="hero">
  <div class="hero-photo" role="img" aria-label="Tropical bay with a cruise ship and city skyline"></div>
  <a class="brand" href="https://boxpoolfreight.example/">
    <span class="brand-dot"></span>
    <span class="brand-name">Rassemblons Nos Caissons</span>
  </a>
  <div class="header-phone">
    <svg width="26" height="26" viewBox="0 0 26 26"><circle cx="13" cy="13" r="12" fill="none" stroke="#fff" stroke-width="1.5"/><path d="M9 7l3 3-2 2c1 2 2 3 4 4l2-2 3 3-2 2c-5 0-10-5-10-10z" fill="#fff"/></svg>
    0800 555 0142
  </div>
  <a class="btn-enquire" href="https://boxpoolfreight.example/Enquire/?subject=Space%20on%20container%20to%20Australia%20-%20Adelaide%20(22.08.2020)">Enquire</a>
  <nav class="main-nav">
    <a href="https://boxpoolfreight.example/">HOME</a>
    <a href="https://boxpoolfreight.example/Containers/">SPACE AVAILABLE</a>
    <a href="#">TRADE ENQUIRIES</a>
    <a href="#">INSURANCE</a>
    <a href="#">CONTACT</a>
  </nav>
  <div class="hero-title hero-welcome">Welcome to</div>
  <div class="hero-title hero-name">Box Pool Freight</div>
  <div class="hero-title hero-find">Find a Container</div>
  <div class="search">
    <div class="search-select">Select Destination
      <svg width="20" height="12" viewBox="0 0 20 12"><path d="M1 1l9 9 9-9" fill="none" stroke="#555" stroke-width="1.6"/></svg>
    </div>
    <div class="search-btn">Find Space</div>
  </div>
  <div class="slide-arrow prev"><svg width="42" height="42" viewBox="0 0 42 42"><path d="M24 13l-8 8 8 8" fill="none" stroke="#fff" stroke-width="2"/></svg></div>
  <div class="slide-arrow next"><svg width="46" height="46" viewBox="0 0 46 46"><path d="M20 15l8 8-8 8" fill="none" stroke="#fff" stroke-width="2.4"/></svg></div>
  <svg class="hero-wave" viewBox="0 0 1200 150" preserveAspectRatio="none">
    <path d="M0 40 Q600 200 1200 46 L1200 150 L0 150Z" fill="#0f2557"/>
    <path d="M0 52 Q600 170 1200 70 L1200 150 L0 150Z" fill="#fff"/>
  </svg>
  <div class="slide-dots"><span></span><span></span><span></span></div>
</section>

<!-- ABOUT -->
<div class="about-photo" role="img" aria-label="Passengers walking on a pier beside a docked cruise ship"></div>
<section class="about-copy">
  <h2>About Us</h2>
  <p>BoxPoolFreight.example is a website that allows you split the cost of international shipping by sharing a container with others - it is that simple.</p>
  <p>Sharing a container reduces the cost of international shipping as you only pay for the space you need. We've got containers heading to destinations around the globe and offer a complete and professional service. Sharing a container means international shipping that's convenient and cost effective.</p>
</section>

<!-- CONTAINERS -->
<section class="containers"></section>
<svg class="section-curve" style="top:1195px" width="1200" height="60" viewBox="0 0 1200 60" preserveAspectRatio="none">
  <path d="M0 52 Q600 -20 1200 52 L1200 0 L0 0Z" fill="#fff"/>
  <path d="M0 52 Q600 -20 1200 52" fill="none" stroke="#b9b9b9" stroke-width="5"/>
</svg>
<h2 class="containers-title">Containers</h2>
<div class="title-rule"></div>

<div class="card-grid">
  <article class="box-card">
    <div class="box-card-head"><div class="box-flag" role="img" aria-label="Australian flag"></div><div class="box-dest">Australia - Adelaide</div><div class="box-space-head">Space Left: 60 ft³</div></div>
    <div class="box-body"><div class="box-space">Space Left: 60 ft³</div><div class="box-bar"><span></span></div>
      <div class="box-meta"><div>Loading Date<br>22.08.2020</div><div>Transit Time<br>4 to 6 weeks</div></div>
      <div class="box-actions"><a class="btn-outline" href="https://boxpoolfreight.example/Containers/">View More</a><a class="btn-solid" href="https://boxpoolfreight.example/Enquire/?subject=Space%20on%20container%20to%20Australia%20-%20Adelaide%20(22.08.2020)">Space Enquire</a></div></div>
  </article>
  <article class="box-card">
    <div class="box-card-head"><div class="box-flag" role="img" aria-label="Australian flag"></div><div class="box-dest">Australia - Adelaide</div><div class="box-space-head">Space Left: 60 ft³</div></div>
    <div class="box-body"><div class="box-space">Space Left: 60 ft³</div><div class="box-bar"><span></span></div>
      <div class="box-meta"><div>Loading Date<br>22.08.2020</div><div>Transit Time<br>4 to 6 weeks</div></div>
      <div class="box-actions"><a class="btn-outline" href="https://boxpoolfreight.example/Containers/">View More</a><a class="btn-solid" href="https://boxpoolfreight.example/Enquire/?subject=Space%20on%20container%20to%20Australia%20-%20Adelaide%20(22.08.2020)">Space Enquire</a></div></div>
  </article>
  <article class="box-card">
    <div class="box-card-head"><div class="box-flag" role="img" aria-label="Australian flag"></div><div class="box-dest">Australia - Adelaide</div><div class="box-space-head">Space Left: 60 ft³</div></div>
    <div class="box-body"><div class="box-space">Space Left: 60 ft³</div><div class="box-bar"><span></span></div>
      <div class="box-meta"><div>Loading Date<br>22.08.2020</div><div>Transit Time<br>4 to 6 weeks</div></div>
      <div class="box-actions"><a class="btn-outline" href="https://boxpoolfreight.example/Containers/">View More</a><a class="btn-solid" href="https://boxpoolfreight.example/Enquire/?subject=Space%20on%20container%20to%20Australia%20-%20Adelaide%20(22.08.2020)">Space Enquire</a></div></div>
  </article>
  <article class="box-card">
    <div class="box-card-head"><div class="box-flag" role="img" aria-label="Australian flag"></div><div class="box-dest">Australia - Adelaide</div><div class="box-space-head">Space Left: 60 ft³</div></div>
    <div class="box-body"><div class="box-space">Space Left: 60 ft³</div><div class="box-bar"><span></span></div>
      <div class="box-meta"><div>Loading Date<br>22.08.2020</div><div>Transit Time<br>4 to 6 weeks</div></div>
      <div class="box-actions"><a class="btn-outline" href="https://boxpoolfreight.example/Containers/">View More</a><a class="btn-solid" href="https://boxpoolfreight.example/Enquire/?subject=Space%20on%20container%20to%20Australia%20-%20Adelaide%20(22.08.2020)">Space Enquire</a></div></div>
  </article>
  <article class="box-card">
    <div class="box-card-head"><div class="box-flag" role="img" aria-label="Australian flag"></div><div class="box-dest">Australia - Adelaide</div><div class="box-space-head">Space Left: 60 ft³</div></div>
    <div class="box-body"><div class="box-space">Space Left: 60 ft³</div><div class="box-bar"><span></span></div>
      <div class="box-meta"><div>Loading Date<br>22.08.2020</div><div>Transit Time<br>4 to 6 weeks</div></div>
      <div class="box-actions"><a class="btn-outline" href="https://boxpoolfreight.example/Containers/">View More</a><a class="btn-solid" href="https://boxpoolfreight.example/Enquire/?subject=Space%20on%20container%20to%20Australia%20-%20Adelaide%20(22.08.2020)">Space Enquire</a></div></div>
  </article>
  <article class="box-card">
    <div class="box-card-head"><div class="box-flag" role="img" aria-label="Australian flag"></div><div class="box-dest">Australia - Adelaide</div><div class="box-space-head">Space Left: 60 ft³</div></div>
    <div class="box-body"><div class="box-space">Space Left: 60 ft³</div><div class="box-bar"><span></span></div>
      <div class="box-meta"><div>Loading Date<br>22.08.2020</div><div>Transit Time<br>4 to 6 weeks</div></div>
      <div class="box-actions"><a class="btn-outline" href="https://boxpoolfreight.example/Containers/">View More</a><a class="btn-solid" href="https://boxpoolfreight.example/Enquire/?subject=Space%20on%20container%20to%20Australia%20-%20Adelaide%20(22.08.2020)">Space Enquire</a></div></div>
  </article>
</div>

<!-- HOW IT WORKS -->
<section class="how">
  <div class="how-photo" role="img" aria-label="Blurred cruise ship behind palm leaves"></div>
</section>
<svg class="section-curve" style="top:2806px" width="1200" height="50" viewBox="0 0 1200 50" preserveAspectRatio="none">
  <path d="M0 45 Q600 -25 1200 45 L1200 0 L0 0Z" fill="#e7e7e7"/>
  <path d="M0 45 Q600 -25 1200 45" fill="none" stroke="#0f2557" stroke-width="6"/>
</svg>
<h2 class="how-title">How it works</h2>
<p class="how-text">Container sharing is a simple and cost effective process when you use Box Pool Freight.</p>
<div class="step step-a">
  <svg width="60" height="58" viewBox="0 0 60 58" fill="none" stroke="#0f2557" stroke-width="2"><path d="M12 26c-6 0-9 5-9 9 0 6 9 15 9 15s9-9 9-15c0-4-3-9-9-9z"/><circle cx="12" cy="35" r="3"/><path d="M46 2c-5 0-7 4-7 7 0 5 7 12 7 12s7-7 7-12c0-3-2-7-7-7z"/><circle cx="46" cy="9" r="2.5"/><path d="M15 52h30c8 0 8-10 0-10H34c-8 0-8-12 2-12h10" stroke-dasharray="3 3"/></svg>
  <span>Simply search for containers by destination Country and port.</span>
</div>
<div class="step step-b">
  <svg width="54" height="56" viewBox="0 0 54 56" fill="none" stroke="#0f2557" stroke-width="2"><rect x="2" y="6" width="50" height="48" rx="3"/><path d="M2 16h50M14 2v8M40 2v8"/><g stroke-width="1.6"><rect x="8" y="22" width="7" height="6"/><rect x="18" y="22" width="7" height="6"/><rect x="28" y="22" width="7" height="6"/><rect x="38" y="22" width="7" height="6"/><rect x="8" y="32" width="7" height="6"/><rect x="18" y="32" width="7" height="6"/><rect x="28" y="32" width="7" height="6"/><rect x="38" y="32" width="7" height="6"/><rect x="8" y="42" width="7" height="6"/><rect x="18" y="42" width="7" height="6"/></g></svg>
  <span>Select a container for sharing by the space available and departure date.</span>
</div>
<div class="step step-c">
  <svg width="52" height="58" viewBox="0 0 52 58" fill="none" stroke="#0f2557" stroke-width="2"><path d="M14 2h26l10 10v44H14z"/><path d="M40 2v10h10"/><path d="M22 10l6 -4 6 4v6H22z"/><rect x="2" y="26" width="26" height="30" rx="2"/><path d="M6 30h18v6H6z"/><g stroke-width="1.6"><path d="M7 41h4M14 41h4M21 41h3M7 46h4M14 46h4M21 46h3M7 51h4M14 51h4M21 51h3"/></g><path d="M32 28h12M32 34h12M32 40h12"/></svg>
  <span>Click to enquire about the container and get your free quote for sharing a container.</span>
</div>
<svg class="abs" style="left:512px;top:3128px" width="26" height="42" viewBox="0 0 26 42" fill="none" stroke="#fff" stroke-width="2.5"><path d="M12 2C2 12 4 28 20 36"/><path d="M13 38l8-1-2-8"/></svg>
<svg class="abs" style="left:812px;top:3250px" width="30" height="42" viewBox="0 0 30 42" fill="none" stroke="#fff" stroke-width="2.5"><path d="M4 40C18 34 22 20 20 6"/><path d="M13 11l7-8 6 9"/></svg>

<!-- ENQUIRY -->
<div class="enquiry-photo" role="img" aria-label="Cruise ship moored in clear blue water"></div>
<h2 class="enquiry-title">Get Enquiries!</h2>
<div class="field field-name">Name</div>
<div class="field field-email">Email</div>
<div class="field field-message">Message</div>
<a class="btn-send" href="https://boxpoolfreight.example/Enquire/?subject=Space%20on%20container%20to%20Australia%20-%20Adelaide%20(22.08.2020)">Send Now
  <svg width="26" height="14" viewBox="0 0 26 14" fill="none" stroke="#fff" stroke-width="2"><path d="M0 7h24M18 1l6 6-6 6"/></svg></a>

<!-- FOOTER -->
<svg class="section-curve" style="top:3988px" width="1200" height="50" viewBox="0 0 1200 50" preserveAspectRatio="none">
  <path d="M0 30 Q600 -16 1200 30 L1200 50 L0 50Z" fill="#0b1c45"/>
  <path d="M0 24 Q600 -22 1200 24" fill="none" stroke="#b9b9b9" stroke-width="6"/>
</svg>
<footer class="footer"></footer>
<div class="footer-brand">Rassemblons Nos Caissons</div>
<div class="socials" aria-label="Social links"><span></span><span></span><span></span></div>
<div class="foot-col contact-col">
  <h4>Contact Us</h4>
  <div class="contact-row"><svg width="14" height="18" viewBox="0 0 14 18" fill="none" stroke="#fff" stroke-width="1.5"><path d="M7 1C3.5 1 1 3.6 1 7c0 4.5 6 10 6 10s6-5.5 6-10c0-3.4-2.5-6-6-6z"/><circle cx="7" cy="7" r="2"/></svg><span>Harlow Quay Limited: Registered<br>Office: 42 Mill Lane, Ashford</span></div>
  <div class="contact-row"><svg width="18" height="18" viewBox="0 0 18 18"><path d="M3 1l4 4-2 2c1 3 3 5 6 6l2-2 4 4-3 2C7 17 1 11 1 4z" fill="#fff"/></svg><span>0800 555 0142</span></div>
  <div class="contact-row"><svg width="18" height="14" viewBox="0 0 18 14" fill="none" stroke="#fff" stroke-width="1.5"><rect x="1" y="1" width="16" height="12"/><path d="M1 1l8 7 8-7"/></svg><span>info@boxpoolfreight.example</span></div>
</div>
<div class="foot-col company-col">
  <h4>Company</h4>
  <a href="https://boxpoolfreight.example/">Home</a>
  <a href="https://boxpoolfreight.example/Containers/">Space Available</a>
  <a href="#">Trade Enquiries</a>
  <a href="#">Insurance</a>
  <a href="#">Stowbay.example</a>
  <a href="#">Crateline.example</a>
  <a href="#">Contact Us</a>
</div>
<div class="foot-col ask-col">
  <h4>Stil have questions?</h4>
  <p>A repesentative will aswer your questions as soon as possible.</p>
  <a class="btn-ask" href="https://boxpoolfreight.example/Enquire/?subject=Space%20on%20container%20to%20Australia%20-%20Adelaide%20(22.08.2020)"><i><svg width="22" height="22" viewBox="0 0 18 18"><path d="M3 1l4 4-2 2c1 3 3 5 6 6l2-2 4 4-3 2C7 17 1 11 1 4z" fill="none" stroke="#fff" stroke-width="1.3"/></svg></i>Space Enquiries</a>
</div>
<div class="foot-bar"></div>
<p class="copyright">Copyright 2020 <strong>Boxpoolfreight</strong>. All Rights Reserved.</p>
<p class="legal"><a href="#">Privacy Policy</a><span>|</span><a href="#">Terms Of Services</a></p>

</body>
</html>
```